Copperfen Hollow Wine And Spirits

We need to design a website for our Liquor Store

Industry/Entity Type

Store

Number of Pages Required

4 page

Requirements
Must have
• Beer, Liquor, Wine & Cigar related theme.
• Mention our 8-locations addresses & maps info
Nice to have
• category for Beer, Liquor & Wine to setup database for item list to link our sql server database.

```html
<!DOCTYPE html>
<html lang="en">
<head>
<meta charset="utf-8">
<title>Copperfen Hollow Wine &amp; Spirits</title>
<link href="https://fonts.googleapis.com/css2?family=Oswald:wght@400;500;600;700&family=Open+Sans:wght@400;600;700&display=swap" rel="stylesheet">
<style>
:root{
  --yellow:#f9cf3f;
  --navy:#1d2d7a;
  --ink:#1b1b1b;
  --blue:#0a2fa8;
  --blue-deep:#082590;
  --dark:#141414;
  --white:#ffffff;
}
*{box-sizing:border-box;margin:0;padding:0}
html,body{width:1200px;height:2643px;overflow:hidden}
body{position:relative;font-family:"Open Sans",Arial,sans-serif;color:var(--white);background:var(--dark)}
.header{position:absolute;left:0;top:0;width:1200px;height:88px;background:var(--yellow)}
.brand{position:absolute;left:100px;top:20px;display:flex;align-items:center;gap:10px;font-family:"Oswald",sans-serif;font-weight:700;font-size:30px;color:var(--navy);letter-spacing:1px}
.brand-mark{width:28px;height:28px;background:var(--navy);border-radius:50%}
.nav{position:absolute;top:36px;left:808px;display:flex;gap:24px;font-family:"Oswald",sans-serif;font-weight:500;font-size:16px;color:var(--ink)}
.nav .active{color:var(--navy)}
.nav-search{position:absolute;left:1086px;top:38px}
.hero{position:absolute;top:88px;left:0;width:1200px;height:474px;background:linear-gradient(90deg,#2a1a10 0%,#5a3a1c 35%,#8a6a44 60%,#3a2a1e 100%)}
.hero-title{position:absolute;left:98px;top:140px;font-family:"Oswald",sans-serif;font-weight:600;font-size:62px;letter-spacing:1px;line-height:1}
.hero-sub{position:absolute;left:100px;top:221px;font-size:25px;font-weight:600}
.btn-ghost{position:absolute;left:100px;top:282px;width:170px;height:48px;border:2px solid var(--white);border-radius:24px;font-family:"Oswald",sans-serif;font-size:15px;display:flex;align-items:center;justify-content:center;letter-spacing:.5px}
.dots{position:absolute;left:568px;top:409px;display:flex;gap:4px}
.dots span{width:12px;height:12px;border:2px solid var(--white);border-radius:50%}
.dots span.on{background:var(--white)}
.about{position:absolute;top:562px;left:0;width:1200px;height:492px;background:radial-gradient(ellipse at 70% 50%,#2c2c2c,#101010 70%)}
.about h2{position:absolute;left:99px;top:54px;font-family:"Oswald",sans-serif;font-weight:500;font-size:38px;line-height:51px}
.about-copy{position:absolute;left:99px;top:176px;width:450px;font-size:14px;line-height:26px}
.about-copy p+p{margin-top:26px}
.btn{display:flex;align-items:center;justify-content:center;background:var(--yellow);color:var(--ink);font-family:"Oswald",sans-serif;font-weight:500;border-radius:22px}
.about .btn{position:absolute;left:99px;top:384px;width:140px;height:44px;font-size:16px}
.about-art{position:absolute;left:630px;top:52px;width:560px;height:390px;border-radius:8px;background:radial-gradient(ellipse at 55% 55%,#6a3a24 0%,#3a2418 45%,rgba(20,20,20,0) 75%)}
.specials{position:absolute;top:1054px;left:0;width:1200px;height:649px;background:linear-gradient(180deg,var(--blue-deep),var(--blue) 50%,var(--blue-deep))}
.specials h2{position:absolute;left:0;width:1200px;top:66px;text-align:center;font-family:"Oswald",sans-serif;font-weight:500;font-size:38px}
.card{position:absolute;top:151px;width:237px}
.card-photo{height:227px}
.card h3{margin-top:22px;font-family:"Oswald",sans-serif;font-weight:500;font-size:21px}
.card p{margin-top:8px;font-size:13.5px;line-height:21px}
.card .btn{margin-top:18px;width:111px;height:35px;font-size:14px}
.map{position:absolute;top:1703px;left:0;width:1200px;height:330px;background:linear-gradient(135deg,#e6e4df,#dcdad4)}
.contact{position:absolute;top:2033px;left:0;width:1200px;height:610px;background:radial-gradient(ellipse at 80% 40%,#3a2e26,#111 70%)}
.contact h2{position:absolute;left:0;width:1200px;top:70px;text-align:center;font-family:"Oswald",sans-serif;font-weight:500;font-size:38px}
.col-title{position:absolute;top:150px;font-family:"Oswald",sans-serif;font-size:15px;font-weight:500}
.label{position:absolute;font-size:11px;font-weight:600}
.field{position:absolute;background:var(--white);height:34px}
.submit{position:absolute;left:634px;top:455px;width:95px;height:33px;font-size:15px}
.loc-head{position:absolute;left:783px;top:178px;display:flex;align-items:center;gap:12px;font-size:15px;font-weight:600}
.pin{width:32px;height:32px;border:2px solid var(--white);border-radius:50%;display:flex;align-items:center;justify-content:center}
.addresses{position:absolute;left:852px;top:226px;list-style:none;font-size:12.5px;line-height:31px}
.addresses li::before{content:"»";position:absolute;left:-20px}
.rule{position:absolute;left:99px;top:530px;width:1002px;height:1px;background:rgba(255,255,255,.25)}
.legal{position:absolute;left:99px;top:558px;font-size:11.5px}
.to-top{position:absolute;left:920px;top:560px}
.social{position:absolute;left:988px;top:555px;display:flex;gap:9px}
.social span{width:32px;height:32px;border:2px solid var(--white);border-radius:50%}
</style>
</head>
<body>
<header class="header">
  <div class="brand"><span class="brand-mark"></span>COPPERFEN HOLLOW</div>
  <nav class="nav"><span class="active">HOME</span><span>SPECIALS</span><span>CONTACT US</span></nav>
  <svg class="nav-search" width="16" height="16" viewBox="0 0 16 16"><circle cx="6.5" cy="6.5" r="5" fill="none" stroke="#1b1b1b" stroke-width="2.2"/><line x1="10.2" y1="10.2" x2="15" y2="15" stroke="#1b1b1b" stroke-width="2.4"/></svg>
</header>

<section class="hero" role="img" aria-label="Couple choosing a bottle of wine in front of store shelves">
  <h1 class="hero-title">COPPERFEN HOLLOW</h1>
  <p class="hero-sub">We are a Liquor Store making wine &amp; spirits.</p>
  <div class="btn-ghost">GET MORE INFO</div>
  <div class="dots"><span class="on"></span><span></span><span></span><span></span></div>
</section>

<section class="about">
  <h2>COPPERFEN HOLLOW WINE<br>&amp; SPIRITS IN FENWICK</h2>
  <div class="about-copy">
    <p>Our extensive wine list includes exquisite collection of finest wines bottles from around the globe.</p>
    <p>Don't see on shelf? Ask us &amp; will order it for you. Large selection craft beer, fine wines, spirits &amp; ONLY walk-in cigar humidor liquor store in Fenwick, INDIANA. Don't see something on shelf? Ask us &amp; will order it for you.</p>
  </div>
  <div class="btn">READ MORE</div>
  <div class="about-art" role="img" aria-label="Wine bottles, beer cans and cigars"></div>
</section>

<section class="specials">
  <h2>OUR SPECIALS</h2>
  <article class="card" style="left:99px">
    <div class="card-photo" role="img" aria-label="Glasses of beer raised in a toast" style="background:linear-gradient(160deg,#3a2a14,#c8891e 60%,#5a3a16)"></div>
    <h3>BEER</h3>
    <p>We carry large selection cold craft beer in Fenwick. If you don't see what you want then we can special order it for you.</p>
    <div class="btn">READ MORE</div>
  </article>
  <article class="card" style="left:354px">
    <div class="card-photo" role="img" aria-label="Glass of whiskey on ice" style="background:linear-gradient(160deg,#1a0e06,#8a4a10 60%,#2a1608)"></div>
    <h3>LIQUOR</h3>
    <p>We carry large selection cold craft beer in Fenwick. If you don't see what you want then we can special order it for you.</p>
    <div class="btn">READ MORE</div>
  </article>
  <article class="card" style="left:609px">
    <div class="card-photo" role="img" aria-label="Two glasses of red wine clinking" style="background:linear-gradient(160deg,#3a2a24,#6a1e22 55%,#1e3a3a)"></div>
    <h3>WINE</h3>
    <p>We carry large selection cold craft beer in Fenwick. If you don't see what you want then we can special order it for you.</p>
    <div class="btn">READ MORE</div>
  </article>
  <article class="card" style="left:864px">
    <div class="card-photo" role="img" aria-label="Open humidor box of cigars" style="background:linear-gradient(160deg,#6a3a1e,#b07a4a 55%,#4a2412)"></div>
    <h3>CIGAR</h3>
    <p>We carry large selection cold craft beer in Fenwick. If you don't see what you want then we can special order it for you.</p>
    <div class="btn">READ MORE</div>
  </article>
</section>

<section class="map" role="img" aria-label="Street map showing the store location on Larkmoor Avenue"></section>

<section class="contact">
  <h2>CONTACT US</h2>
  <div class="col-title" style="left:99px">CONTACT FORM</div>
  <span class="label" style="left:99px;top:196px">NAME :</span>
  <span class="label" style="left:418px;top:196px">SUBJECT</span>
  <div class="field" style="left:99px;top:220px;width:312px"></div>
  <div class="field" style="left:418px;top:220px;width:311px"></div>
  <span class="label" style="left:99px;top:268px">EMAIL</span>
  <span class="label" style="left:418px;top:268px">MOBILE</span>
  <div class="field" style="left:99px;top:292px;width:312px"></div>
  <div class="field" style="left:418px;top:292px;width:311px"></div>
  <span class="label" style="left:99px;top:337px">MESSAGE :</span>
  <div class="field" style="left:99px;top:358px;width:630px;height:83px"></div>
  <div class="btn submit">SUBMIT</div>

  <div class="col-title" style="left:783px">LOCATION</div>
  <div class="loc-head">
    <span class="pin"><svg width="12" height="16" viewBox="0 0 12 16"><path d="M6 0C2.7 0 0 2.6 0 5.9 0 10 6 16 6 16s6-6 6-10.1C12 2.6 9.3 0 6 0z" fill="#f9cf3f"/><circle cx="6" cy="6" r="2.2" fill="#111"/></svg></span>
    Copperfen Hollow Wine &amp; Spirits
  </div>
  <ul class="addresses">
    <li>2406 Larkmoor Ave, Fenwick, IN 47912</li>
    <li>5172 Hartwell Ave, Fenwick, IN 47918</li>
    <li>6390 Millstone Way, Fenwick, IN 47925</li>
    <li>517 Cedar St, Alderbrook, IN 47931</li>
    <li>728 Thornfield Rd, Fenwick, IN 47918</li>
    <li>2981 Quarry Rd, Fenwick, IN 47914</li>
    <li>8034 Willowbank St, Fenwick, IN 47916</li>
    <li>1647 Fairlow Dr, Fenwick, IN 47925</li>
  </ul>

  <div class="rule"></div>
  <p class="legal">Copyrights © 2017, Copperfen Hollow . All Rights Reserved.&nbsp; About &nbsp;|&nbsp; Privacy statement &nbsp;|&nbsp; Disclaimer</p>
  <svg class="to-top" width="28" height="18" viewBox="0 0 28 18"><polyline points="3,15 14,4 25,15" fill="none" stroke="#fff" stroke-width="3"/></svg>
  <div class="social" aria-label="Social links"><span></span><span></span><span></span></div>
</section>
</body>
</html>
```